Business Card Design for Kidvale (Hires out childrens play areas)

Looking to have a business card designed for a company we just bought. The company rents out childrens play areas.

I have uploaded a couple of examples of the kind of business card style I like. Here are two more examples:

https://quorvastudio.nz/project/bright-romp-branding/
https://imgvaultcdn.com/design_img/8841052/302917/302917_5518203_8841052_b73e19a2_image.jpg

I think a white card will be best due to all the colours in the logo.

Size we require: 3.75" x 2.25" (horizontally orientated) with a 0.125" bleed

Uploaded is two versions of our logo.

Details for the card:
1. My name: Liam Verster
2. Title: Managing Director
3. Phone no: 021 563 417
4. Email: liam@kidvale.co.nz
5. URL: www.kidvale.co.nz
6. Address:
PO Box 318625
Fernlea, Auckland

Let me know if you need anything else.

Target Market(s)

Hospitals, doctors surgeries, bed shops, etc.

Contact Information for Business Card

Details for the card:
1. My name: Liam Verster
3. Phone no: 021 563 417
5. URL: www.kidvale.co.nz
6. Address:
PO Box 318625
Fernlea, Auckland

Requirements
Should not have
• Not too busy.

```html
<!DOCTYPE html>
<html lang="en">
<head>
<meta charset="utf-8">
<title>Kidvale Business Card</title>
<link rel="stylesheet" href="https://fonts.googleapis.com/css2?family=Montserrat:wght@400;500;700&display=swap">
<style>
  :root {
    --canvas-bg: #e9ebee;
    --card-bg: #ffffff;
    --pattern-tint: #fafafa;
    --accent: #d9552b;
    --ink: #2f2f2f;
    --ink-soft: #4a4a4a;
    --brand: #2a6db5;
  }
  * { margin: 0; padding: 0; box-sizing: border-box; }
  html, body { width: 1200px; height: 800px; overflow: hidden; }
  body {
    background: var(--canvas-bg);
    font-family: "Montserrat", Arial, sans-serif;
    display: flex;
    align-items: center;
    justify-content: center;
    gap: 40px;
  }
  .card {
    position: relative;
    width: 560px;
    height: 336px;
    background: var(--card-bg);
    box-shadow: 0 2px 10px rgba(0,0,0,0.12);
    overflow: hidden;
  }
  .toy-pattern {
    position: absolute;
    inset: 0;
    background: var(--pattern-tint);
  }
  .brand {
    position: absolute;
    display: flex;
    align-items: center;
    gap: 14px;
    color: var(--brand);
    font-weight: 700;
    white-space: nowrap;
  }
  .brand-dot {
    width: 34px; height: 34px; border-radius: 50%;
    background: var(--brand);
    flex: none;
  }
  .card-front .brand { left: 50%; top: 50%; transform: translate(-50%, -50%); font-size: 56px; }
  .card-front .brand-dot { width: 48px; height: 48px; }
  .card-back .brand { left: 42px; top: 50%; transform: translateY(-50%); font-size: 38px; }
  .details {
    position: absolute;
    left: 320px;
    top: 48px;
    width: 220px;
    color: var(--ink);
  }
  .person-name { color: var(--accent); font-weight: 700; font-size: 24px; line-height: 1.1; }
  .person-title { font-size: 16px; margin-top: 4px; }
  .divider { width: 36px; height: 3px; background: var(--accent); margin: 16px 0 18px; }
  .address { font-size: 12px; line-height: 1.45; color: var(--ink-soft); margin-bottom: 16px; }
  .contact-list { list-style: none; font-size: 13px; }
  .contact-list li { display: flex; align-items: center; gap: 10px; margin-bottom: 8px; }
  .contact-icon { width: 18px; height: 18px; flex: none; }
</style>
</head>
<body>
  <section class="card card-front" aria-label="Card front">
    <div class="toy-pattern" role="img" aria-label="Faint line doodles of children's toys: blocks, balls, boats, robots, planes"></div>
    <div class="brand"><span class="brand-dot"></span><span>Kidvale</span></div>
  </section>

  <section class="card card-back" aria-label="Card back">
    <div class="toy-pattern" role="img" aria-label="Faint line doodles of children's toys: rattles, cars, kites, birds"></div>
    <div class="brand"><span class="brand-dot"></span><span>Kidvale</span></div>
    <div class="details">
      <p class="person-name">Liam Verster</p>
      <p class="person-title">Managing Director</p>
      <div class="divider"></div>
      <p class="address">PO Box 318625<br>Fernlea, Auckland</p>
      <ul class="contact-list">
        <li>
          <svg class="contact-icon" viewBox="0 0 18 18"><circle cx="9" cy="9" r="9" fill="var(--accent)"/><path d="M6 5.2l1.6-.4 1 2.2-1 .8a5 5 0 0 0 2.6 2.6l.8-1 2.2 1-.4 1.6c-3.6.3-7.1-3.2-6.8-6.8z" fill="#fff"/></svg>
          <span>021 563 417</span>
        </li>
        <li>
          <svg class="contact-icon" viewBox="0 0 18 18"><circle cx="9" cy="9" r="9" fill="var(--accent)"/><rect x="4.8" y="6" width="8.4" height="6" fill="none" stroke="#fff" stroke-width="1.1"/><path d="M4.8 6L9 9.3 13.2 6" fill="none" stroke="#fff" stroke-width="1.1"/></svg>
          <span>liam@kidvale.co.nz</span>
        </li>
        <li>
          <svg class="contact-icon" viewBox="0 0 18 18"><circle cx="9" cy="9" r="9" fill="var(--accent)"/><g fill="none" stroke="#fff" stroke-width="1"><circle cx="9" cy="9" r="4.4"/><ellipse cx="9" cy="9" rx="1.9" ry="4.4"/><path d="M4.6 9h8.8"/></g></svg>
          <span>www.kidvale.co.nz</span>
        </li>
      </ul>
    </div>
  </section>
</body>
</html>
```